Business Card Design

I want to pull elements/colors from Website. Attached is a screen shot. Do not want any buildings/building graphics/construction clichés. This is for a construction management firm but I want to keep it broad enough that I can expand into other areas. I do not want the logo to be limited. Thank you.
Updates

Please review the screen shot of the website. Please use the font and color of Brackwell Ventures, LLC on the website. Please use the tag line "Construction Management in the Palm Beaches" Please show contractor license ... CGC 4093615 You may use the back for the contact information. Please no phone/house icons. It does not have to be a black card. Thank you.

Target Market(s)

Professional people with money. Owners, Architects, Engineers, Developers, Real Estate Agents etc.

Industry/Entity Type

Construction

Contact Information for Business Card

Brackwell Ventures, LLC
Construction Management

Dale T Brackwell
240 Marlidge Court #14
North Palm Beach, FL 33408
(561) 555-0187
www.BrackwellVentures.example

Requirements
Must have
• Clean, crisp, modern.

Broad enough that it is not trapped into a particular industry.

My goal is to expand into different markets, different industries.

Should not have
• The back of the card should not be colored in any way. Rubs off on other cards.

Do not want any buildings/building graphics/construction clichés.

```html
<!DOCTYPE html>
<html lang="en">
<head>
<meta charset="utf-8">
<title>Brackwell Ventures – Business Card</title>
<link rel="stylesheet" href="https://fonts.googleapis.com/css2?family=Open+Sans:wght@400;700&display=swap">
<style>
  :root {
    --page: #e9e7e5;
    --card-base: #2a2525;
    --facet-left: #3a3333;
    --facet-right: #433b3b;
    --facet-edge: #332d2d;
    --ink: #ffffff;
    --ink-soft: #d9d4d2;
  }
  * { margin: 0; padding: 0; box-sizing: border-box; }
  html, body { width: 1200px; height: 1000px; overflow: hidden; }
  body {
    background: var(--page);
    font-family: "Open Sans", Arial, sans-serif;
    display: flex; align-items: center; justify-content: center;
  }
  .business-card {
    position: relative;
    width: 1000px; height: 571px;
    background: var(--card-base);
    box-shadow: 0 14px 40px rgba(0,0,0,.25);
    overflow: hidden;
    color: var(--ink);
  }
  .card-facets { position: absolute; inset: 0; }
  .card-content {
    position: absolute; inset: 0;
    display: flex; flex-direction: column; align-items: center;
    text-align: center;
    padding-top: 34px;
  }
  .card-content p, .card-content h1 { line-height: 1.05; white-space: nowrap; }
  .brand-dot {
    width: 88px; height: 88px; border-radius: 50%;
    background: var(--ink);
  }
  .brand-name {
    font-weight: 700; font-size: 50px;
    margin-top: 14px; letter-spacing: .2px;
  }
  .brand-tagline {
    font-weight: 400; font-size: 28px;
    margin-top: 8px; letter-spacing: .4px;
  }
  .person-name { font-size: 40px; font-weight: 400; margin-top: 26px; }
  .license { font-size: 22px; color: var(--ink-soft); margin-top: 8px; letter-spacing: 1px; }
  .contact-phone { font-size: 32px; margin-top: 28px; }
  .contact-address { font-size: 34px; margin-top: 20px; }
  .contact-web { font-size: 28px; margin-top: 20px; }
</style>
</head>
<body>
  <article class="business-card">
    <svg class="card-facets" viewBox="0 0 1000 571" preserveAspectRatio="none" aria-hidden="true">
      <polygon points="0,0 600,0 560,60 0,571" fill="var(--facet-left)"/>
      <polygon points="600,0 1000,0 1000,300 560,60" fill="var(--facet-right)"/>
      <polygon points="0,330 0,571 120,571" fill="var(--facet-edge)"/>
    </svg>
    <div class="card-content">
      <div class="brand-dot"></div>
      <h1 class="brand-name">Brackwell Ventures</h1>
      <p class="brand-tagline">Construction Management in the Palm Beaches</p>
      <p class="person-name">Dale T Brackwell</p>
      <p class="license">CGC 4093615</p>
      <p class="contact-phone">(561) 555-0187</p>
      <p class="contact-address">240 Marlidge Court, #14 North Palm Beach, FL 33408</p>
      <p class="contact-web">www.BrackwellVentures.example</p>
    </div>
  </article>
</body>
</html>
```